Solar Company Bussiness Card

I need a 2 sided business card and would like a .psd and any font files for each side of the card. I would like my logo used, it should be attached with the fonts. I'm not opposed to the font colors with the logo being changed.

On the sample design, I'd like the following:

Darren Pellow
President
Phone: 555-318-2947
www.sunvaleenergyco.example

As I've recently opened in a 2nd market, I'm not sure about an address as I currently have 2 of them. I may actually get separate cards printed, one batch for each address, that's why I need the PSD file.
Updates

I'm very pleased with the response and designs I've received here for my business card. First and foremost, I'd like to thank everyone who took the time to submit a design. There truly are a lot of great designs in the bunch here and I'm having a little difficulty deciding. I will be reaching out to someone in the next day or two here to go to a final design. At this time, I'm not looking for any new concepts. If any of you do logos, I'm looking for a new logo for our sister entity, Pellow Partners, Inc. Thanks, Darren Pellow

Reason: I'm not looking for any new designs at this point, but extending this deadline in order to give people I've asked a chance to re-submit items.

Industry/Entity Type

Business

```html
<!DOCTYPE html>
<html lang="en">
<head>
<meta charset="utf-8">
<title>Sunvale Energy – Business Card</title>
<link href="https://fonts.googleapis.com/css2?family=Open+Sans:wght@400;600&display=swap" rel="stylesheet">
<style>
  :root {
    --backdrop: #e4e6e8;
    --card: #ffffff;
    --card-edge: #f1f2f3;
    --brand-blue: #2a7cc4;
    --accent-blue: #2f86d0;
    --ink: #2e2e2e;
    --icon: #1f5f9a;
  }
  * { margin: 0; padding: 0; box-sizing: border-box; }
  html, body {
    width: 1200px; height: 871px; overflow: hidden;
    background: var(--backdrop);
    font-family: "Open Sans", Arial, sans-serif;
  }
  .sheet {
    position: relative; width: 1200px; height: 871px;
  }
  .card {
    position: absolute;
    width: 616px; height: 352px;
    overflow: hidden;
    background: linear-gradient(135deg, var(--card) 60%, var(--card-edge));
    box-shadow: 0 6px 18px rgba(0,0,0,0.18);
  }
  .card--front { left: 120px; top: 56px; }
  .card--back  { left: 464px; top: 463px; }

  .wordmark {
    display: flex; align-items: center; gap: 12px;
    color: var(--brand-blue);
    font-weight: 600;
    letter-spacing: 0.5px;
    white-space: nowrap;
  }
  .wordmark__square {
    background: var(--brand-blue);
  }
  .card--front .wordmark {
    position: absolute; left: 50%; top: 50%;
    transform: translate(-50%, -50%);
    font-size: 40px;
  }
  .card--front .wordmark__square { width: 34px; height: 34px; }

  .card--back .wordmark {
    position: absolute; left: 40px; top: 40px;
    font-size: 30px;
  }
  .card--back .wordmark__square { width: 26px; height: 26px; }

  .contact {
    position: absolute; left: 318px; top: 176px;
    color: var(--ink);
  }
  .contact__name {
    font-size: 20px; letter-spacing: 0.8px; line-height: 1.2;
  }
  .contact__title {
    font-size: 15px; color: var(--accent-blue); letter-spacing: 0.6px;
    margin-bottom: 22px;
  }
  .contact__row {
    display: flex; align-items: center; gap: 14px;
    font-size: 15px; letter-spacing: 1.4px; margin-left: -34px;
    height: 28px; white-space: nowrap;
  }
  .contact__icon { width: 20px; height: 20px; flex: none; }
</style>
</head>
<body>
<main class="sheet">
  <section class="card card--front" aria-label="Card front">
    <div class="wordmark">
      <span class="wordmark__square"></span>
      <span class="wordmark__name">Sunvale Energy</span>
    </div>
  </section>

  <section class="card card--back" aria-label="Card back">
    <div class="wordmark">
      <span class="wordmark__square"></span>
      <span class="wordmark__name">Sunvale Energy</span>
    </div>

    <div class="contact">
      <p class="contact__name">Darren Pellow</p>
      <p class="contact__title">President</p>
      <p class="contact__row">
        <svg class="contact__icon" viewBox="0 0 20 20" aria-hidden="true">
          <path d="M2 7c0-3 4-4 8-4s8 1 8 4l-3 1-1-2H6L5 8z" fill="var(--icon)"/>
          <rect x="4" y="9" width="12" height="8" rx="2" fill="none" stroke="var(--icon)" stroke-width="1.8"/>
          <circle cx="10" cy="13" r="2" fill="var(--icon)"/>
        </svg>
        <span>555-318-2947</span>
      </p>
      <p class="contact__row">
        <svg class="contact__icon" viewBox="0 0 20 20" aria-hidden="true">
          <circle cx="10" cy="10" r="8" fill="none" stroke="var(--icon)" stroke-width="1.8"/>
          <ellipse cx="10" cy="10" rx="3.5" ry="8" fill="none" stroke="var(--icon)" stroke-width="1.4"/>
          <line x1="2" y1="10" x2="18" y2="10" stroke="var(--icon)" stroke-width="1.4"/>
        </svg>
        <span>www.sunvaleenergyco.example</span>
      </p>
    </div>
  </section>
</main>
</body>
</html>
```